Custom Real Estate Postcard for Buying Communities

We are a real estate company that owns/operates mobile home parks and want to send out a postcard to owners of these communities letting them know who our company is and let them know we want to buy their community. We are looking to create a postcard that introduces our company to the owner and also lets them know we want to buy their community - we are targeting older mom & pop type communities so we would like the postcard to have a home-y feel that makes the owner feel like our company will treat them fairly during the acquisition process
I have attached a few images from our communities that might look good on a postcard - you don't need to use all of them, I just included multiple so there are different options. please feel free to edit/enhance the images if needed.
Our company is Bright Meadow Holdings (BMH) and the logo is attached.
Text to be included somewhere on postcard: "We pride ourselves on active hands-on management in order to provide our residents quality communities at an affordable price.
BMH is a proven owner/operator and has the ability to purchase without any financing contingencies.
We provide a quick and easy closing. We do not retrade
Target Market(s)
Owners of Mobile Home Parks that BMH (our company) would like to acquire - small mom & pop owners that want to see that we aren't the big firm trying to come in and take over but a local company that will still treat the residents well
Industry/Entity Type
Real Estate
Colors
Designer to choose colors to be used in the design.
Requirements
Must have
- The BMH logo, at least one picture of a mobile home park from the attached pictures. And some version/form of the provided text. Info/contact section with website (www.bmhparks.example), email (info@bmhparks.example) and phone (555.284.7160)
- Something sort of call to action like: "We Want to Buy Your Community", "Ready to Sell?", "Interested in Selling?" etc.
Nice to have
- BMH Logo Colors, in addition to any other colors if designer thinks there are complimentary colors

```html
<!DOCTYPE html>
<html lang="en">
<head>
<meta charset="utf-8">
<title>Bright Meadow Holdings – Postcard</title>
<link href="https://fonts.googleapis.com/css2?family=Montserrat:wght@400;500;700;800;900&family=Open+Sans:wght@300;400&display=swap" rel="stylesheet">
<style>
  :root {
    --frame: #564b48;
    --paper: #ffffff;
    --brick: #8a2e1c;
    --rose: #d98080;
    --rose-light: #eeb3ad;
    --ink: #1b1b1b;
    --logo-ink: #2a2422;
    --sky: #3f8fd6;
    --leaf: #4f7a2f;
    --grass: #6ea03a;
  }
  * { margin: 0; padding: 0; box-sizing: border-box; }
  html, body { width: 927px; height: 1200px; overflow: hidden; }
  body {
    background: var(--frame);
    position: relative;
    font-family: "Montserrat", Arial, sans-serif;
    color: var(--ink);
  }
  .card {
    position: absolute;
    left: 25px;
    width: 876px;
    background: var(--paper);
    overflow: hidden;
  }
  .card--front { top: 25px; height: 566px; }
  .card--back { top: 607px; height: 568px; }

  .front-art { position: absolute; inset: 0; width: 876px; height: 566px; display: block; }

  .brand {
    position: absolute;
    left: 40px;
    top: 470px;
    display: flex;
    align-items: center;
    gap: 14px;
  }
  .brand__mark { width: 40px; height: 40px; background: var(--brick); }
  .brand__name {
    font-family: "Open Sans", Arial, sans-serif;
    font-weight: 300;
    font-size: 25px;
    line-height: 27px;
    letter-spacing: 1.5px;
    text-transform: uppercase;
    color: var(--logo-ink);
  }

  .headline {
    position: absolute;
    right: 71px;
    top: 470px;
    font-family: "Montserrat", Arial, sans-serif;
    font-weight: 900;
    font-size: 34px;
    line-height: 30px;
    color: var(--brick);
    letter-spacing: -0.5px;
    text-align: right;
  }
  .headline span { display: block; }
  .headline span:first-child { margin-right: 58px; }

  .intro {
    position: absolute;
    left: 45px;
    top: 28px;
    width: 300px;
    font-size: 12.5px;
    line-height: 19.5px;
    font-weight: 500;
  }
  .intro p + p { margin-top: 8px; }

  .aerial {
    position: absolute;
    left: 0;
    top: 162px;
    width: 378px;
    height: 406px;
    background: linear-gradient(to bottom,
      #ffffff 0%, #f4f6f5 14%, #cfd8d4 26%, #7d9168 40%,
      #5f8a3a 55%, #6d9a44 75%, #5a823a 100%);
  }
  .contact {
    position: absolute;
    left: 45px;
    top: 180px;
  }
  .contact__phone {
    font-weight: 800;
    font-size: 41px;
    line-height: 46px;
    letter-spacing: -0.5px;
  }
  .contact__line {
    font-weight: 500;
    font-size: 16px;
    line-height: 22px;
  }
  .contact__phone + .contact__line { margin-top: 14px; }
</style>
</head>
<body>

<section class="card card--front">
  <svg class="front-art" viewBox="0 0 945 611" preserveAspectRatio="none" aria-hidden="false">
    <defs>
      <linearGradient id="photoTone" x1="0" y1="0" x2="0" y2="1">
        <stop offset="0" stop-color="#3a6a2c"/>
        <stop offset="0.3" stop-color="#5a8a3c"/>
        <stop offset="0.52" stop-color="#cfd3cc"/>
        <stop offset="0.62" stop-color="#8aa657"/>
        <stop offset="0.8" stop-color="#9a9d9c"/>
        <stop offset="1" stop-color="#7b9b45"/>
      </linearGradient>
    </defs>
    <rect x="0" y="0" width="945" height="560" fill="url(#photoTone)" role="img" aria-label="Photo of a manufactured home community street with homes under tall trees"/>
    <path class="swoosh swoosh--light" d="M0,300 C40,400 240,450 520,462 C720,470 880,500 945,525 L945,611 L0,611 Z" fill="var(--rose-light)"/>
    <path class="swoosh swoosh--rose" d="M0,318 C50,410 250,458 530,470 C720,478 880,505 945,532 L945,611 L0,611 Z" fill="var(--rose)"/>
    <path class="paper-curve" d="M0,365 C70,435 280,468 540,475 C730,480 890,505 945,545 L945,611 L0,611 Z" fill="#ffffff"/>
  </svg>

  <div class="brand">
    <div class="brand__mark"></div>
    <div class="brand__name">Bright<br>Meadow<br>Holdings</div>
  </div>

  <h1 class="headline"><span>We Want to Buy</span><span>Your Community</span></h1>
</section>

<section class="card card--back">
  <div class="intro">
    <p>We pride ourselves on active hands-on management in order to provide our residents quality communities at an affordable price.</p>
    <p>BMH is a proven owner/operator and has the ability to purchase without any financing contingencies.</p>
  </div>

  <div class="aerial" role="img" aria-label="Aerial photo of a manufactured home community among green fields and trees, fading into morning mist"></div>

  <div class="contact">
    <div class="contact__phone">555.284.7160</div>
    <div class="contact__line">info@bmhparks.example</div>
    <div class="contact__line">www.bmhparks.example</div>
  </div>
</section>

</body>
</html>
```